Whispers From Distant Stars Poster

So Last year One of the Great Designers from here Came up with a poster for my Events... But Now it is Time to freshen it up.. I have attached the original poster.. I would like the Same wording.. Same Picture of me,. Just fresh Design and colours for the new event year ahead.
This Poster Will be used in Theatres and Hall to Advertise our Event so it needs to stand out but still remain classy
I would Also need The Final Version to be delivered in PhotoShop Version so That I Can Alter Things like the Venue Name, Date, and Ticket Details,, As they change all the time.
Events

```html
<!DOCTYPE html>
<html lang="en">
<head>
<meta charset="utf-8">
<title>Whispers From Distant Stars – Event Poster</title>
<link href="https://fonts.googleapis.com/css2?family=Great+Vibes&family=Tinos:wght@400;700&display=swap" rel="stylesheet">
<style>
  :root{
    --stage:#020b1a;
    --sky-light:#f3f6fb;
    --sky-mid:#c9d5ea;
    --sky-deep:#93a8cc;
    --navy:#0b1d47;
    --navy-deep:#071437;
    --title-grey:#4f5158;
    --silver-dark:#55565c;
    --silver-light:#d9dade;
    --oval:#5f7197;
    --gold-light:#f2d97a;
    --gold:#c99a2e;
    --name:#3a3a44;
    --venue:#e8dc6a;
    --white:#ffffff;
  }
  *{margin:0;padding:0;box-sizing:border-box}
  html,body{width:730px;height:1200px;overflow:hidden;background:var(--stage)}
  .canvas{position:relative;width:730px;height:1200px;background:var(--stage)}

  .poster{
    position:absolute;left:76px;top:120px;width:578px;height:822px;overflow:hidden;
    font-family:"Tinos","Times New Roman",serif;
  }
  .sky{
    position:absolute;inset:0;
    background:
      radial-gradient(ellipse 60% 45% at 52% 28%, var(--white) 0%, rgba(255,255,255,0) 70%),
      linear-gradient(180deg, var(--sky-mid) 0%, var(--sky-light) 40%, var(--sky-deep) 62%, var(--sky-light) 86%);
  }
  .night-band{
    position:absolute;left:0;right:0;top:610px;bottom:0;
    background:linear-gradient(180deg, rgba(11,29,71,0) 0%, var(--navy) 20%, var(--navy-deep) 100%);
  }
  .portrait{
    position:absolute;left:272px;top:172px;width:306px;height:532px;
    border-radius:120px 120px 0 0;
    background:linear-gradient(180deg, #c7a596 0%, #b99486 22%, #e9edf3 36%, #2a2f3b 55%, #171b26 85%, rgba(11,29,71,0) 100%);
  }

  .title{position:absolute;left:0;right:0;top:30px;text-align:center}
  .title-lead{
    display:block;font-size:36px;color:var(--title-grey);letter-spacing:0.5px;line-height:1;
  }
  .title-lead .small{font-size:24px}
  .title-script{
    display:block;margin-top:-6px;
    font-family:"Great Vibes",cursive;font-size:150px;line-height:1.05;
    background:linear-gradient(180deg, var(--silver-light) 0%, var(--silver-dark) 55%, var(--silver-light) 100%);
    -webkit-background-clip:text;background-clip:text;color:transparent;
  }

  .tagline{
    position:absolute;left:46px;top:264px;width:218px;height:94px;
    border-radius:50%;background:var(--oval);border:1px solid rgba(255,255,255,0.55);
    display:flex;align-items:center;justify-content:center;text-align:center;
    color:var(--white);font-size:13px;letter-spacing:2px;line-height:1.5;
  }

  .laurel{
    position:absolute;left:18px;top:404px;width:236px;height:224px;border-radius:50%;
    background:radial-gradient(circle, rgba(242,217,122,0) 52%, var(--gold-light) 62%, var(--gold) 72%, rgba(201,154,46,0) 80%);
  }
  .medium{
    position:absolute;left:18px;top:456px;width:236px;text-align:center;color:var(--name);
  }
  .medium-name{font-weight:700;font-size:42px;line-height:0.95;letter-spacing:-1px}
  .medium-role{margin-top:6px;font-size:13px;line-height:1.3}

  .details{position:absolute;left:0;right:0;top:700px;text-align:center;color:var(--white)}
  .date{font-size:34px;line-height:1.2}
  .date sup{font-size:16px}
  .venue{margin-top:8px;font-size:16px;letter-spacing:1.2px;color:var(--venue)}
  .tickets{margin-top:4px;font-size:16px;letter-spacing:1px}
</style>
</head>
<body>
<div class="canvas">
  <section class="poster">
    <div class="sky" role="img" aria-label="Photograph of bright clouds with rays of light"></div>
    <div class="portrait" role="img" aria-label="Photograph of the medium in a dark suit, reaching out his hand"></div>
    <div class="night-band"></div>

    <h1 class="title">
      <span class="title-lead"><span class="small">WHISPERS FROM</span> DISTANT</span>
      <span class="title-script">Stars</span>
    </h1>

    <p class="tagline">AN EVENING OF<br>MEDIUMSHIP</p>

    <div class="laurel" role="img" aria-label="Gold laurel wreath"></div>
    <div class="medium">
      <p class="medium-name">RHYS<br>CALLOWAY</p>
      <p class="medium-role">Renowned Spiritualist<br>Medium</p>
    </div>

    <div class="details">
      <p class="date">Monday, 21<sup>st</sup> of November</p>
      <p class="venue">Harbour Lights Theatre PENRHOS</p>
      <p class="tickets">For tickets, call box office 01632960418</p>
    </div>
  </section>
</div>
</body>
</html>
```